MEDITERRANEAN Cafe Website needed

We are a MEDITERRANEAN Café serving Coffee, breakfast, Pizza, Pasta, Sandwiches etc.

We need a home page, menu & venue, Reservations & Events, Delivery
Connect (Social media / Feedback / Contact us),Join our team
Updates

Can we keep the designs in Mediterranean colours, look, and feel pleasethanks Added Saturday, December 10, 2016

Project Deadline Extended Reason: I have guarantied the payment and upgraded the project. I would like this would to give more time for new designs to come in and a couple of potential designs to show more. Added Sunday, December 11, 2016

Industry/Entity Type

Cafe

Coding

Coded - Design and coding required

Number of Pages Required

5+ page

Requirements
Must have
• MEDITERRANEAN feel, colours, style etc.
• http://www.quillandfen (DOT) co (DOT) uk
Nice to have

```html
<!DOCTYPE html>
<html lang="en">
<head>
<meta charset="utf-8">
<title>Lumera Cafe – About Us</title>
<link href="https://fonts.googleapis.com/css2?family=Jost:wght@300;400;500;600&family=Great+Vibes&display=swap" rel="stylesheet">
<style>
  :root {
    --teal: #1d6272;
    --red: #d8142a;
    --paper: #f0dfbf;
    --paper-dark: #e2c99c;
    --ink: #6b5a48;
    --footer-ink: #4a3f35;
    --white: #ffffff;
  }
  * { box-sizing: border-box; margin: 0; padding: 0; }
  html, body { width: 811px; height: 1200px; overflow: hidden; }
  body {
    position: relative;
    font-family: "Jost", sans-serif;
    background: radial-gradient(ellipse at 30% 40%, #f5e6c8 0%, var(--paper) 45%, var(--paper-dark) 100%);
    color: var(--ink);
  }
  .site-header {
    position: absolute; left: 0; top: 0; width: 811px; height: 74px;
    background: rgba(255, 250, 240, 0.94);
    border-bottom: 1px solid #e8dcc8;
  }
  .brand {
    position: absolute; left: 131px; top: 30px;
    display: flex; align-items: center; gap: 4px;
    font-size: 9.5px; font-weight: 600; color: var(--teal); letter-spacing: 0.4px;
    white-space: nowrap;
  }
  .brand-dot { width: 8px; height: 8px; border-radius: 50%; background: var(--teal); }
  .main-nav {
    position: absolute; left: 223px; top: 32px; width: 370px;
    display: flex; justify-content: space-between;
    font-size: 8px; font-weight: 500; color: var(--teal); white-space: nowrap;
  }
  .main-nav .is-active { color: var(--red); }
  .book-button {
    position: absolute; left: 604px; top: 27px; width: 76px; height: 21px;
    background: var(--red); color: var(--white);
    font-size: 9px; font-weight: 500; text-align: center; line-height: 21px; white-space: nowrap;
  }
  .hero {
    position: absolute; left: 0; top: 74px; width: 811px; height: 201px;
    background: linear-gradient(100deg, #5f7d3a 0%, #8aa34d 25%, #c98b5d 50%, #e9b04a 70%, #f2d48a 100%);
  }
  .section-title {
    position: absolute; left: 0; top: 317px; width: 811px; text-align: center;
    font-size: 23px; font-weight: 500; color: var(--teal); letter-spacing: -0.3px;
  }
  .about-text {
    position: absolute; left: 130px; top: 356px; width: 551px; height: 104px;
    background: rgba(255, 250, 240, 0.35);
    padding: 14px 14px; font-size: 10.4px; font-weight: 300; line-height: 18.4px; color: var(--ink);
    letter-spacing: 0.15px;
  }
  .promo-card {
    position: absolute; top: 487px; width: 262px; height: 155px;
    text-align: center; color: var(--white);
  }
  .promo-card.breakfast { left: 130px; background: linear-gradient(135deg, #8a7868, #c8b8a6 55%, #a88c6a); }
  .promo-card.location { left: 418px; background: linear-gradient(135deg, #3d2418, #6b3c24 55%, #8a5a38); }
  .promo-lead { position: absolute; top: 30px; width: 100%; font-size: 13px; font-weight: 300; }
  .promo-script { position: absolute; top: 40px; width: 100%; font-family: "Great Vibes", cursive; font-size: 44px; }
  .cta {
    position: absolute; background: var(--red); color: var(--white);
    font-weight: 500; display: flex; align-items: center; justify-content: center; gap: 6px; white-space: nowrap;
  }
  .promo-card .cta { left: 79px; top: 107px; width: 105px; height: 25px; font-size: 10.5px; }
  .cta svg { width: 7px; height: 9px; }
  .menu-banner {
    position: absolute; left: 131px; top: 671px; width: 550px; height: 218px;
    background: linear-gradient(90deg, #d9a66c 0%, #b8794a 40%, #6e3f28 75%, #5a3220 100%);
    color: var(--white); text-align: center;
  }
  .banner-line1 { position: absolute; top: 33px; width: 100%; font-size: 15px; font-weight: 300; }
  .banner-line2 { position: absolute; top: 52px; width: 100%; font-size: 26px; font-weight: 400; }
  .banner-line2 .script { font-family: "Great Vibes", cursive; font-size: 50px; vertical-align: -6px; }
  .banner-line2 .small { font-size: 19px; }
  .banner-line3 { position: absolute; top: 110px; width: 100%; font-size: 12px; font-weight: 300; }
  .banner-line4 { position: absolute; top: 124px; width: 100%; font-size: 19px; font-weight: 400; }
  .menu-banner .cta { left: 217px; top: 163px; width: 115px; height: 22px; font-size: 8.5px; }
  .social-title {
    position: absolute; left: 0; top: 936px; width: 811px; text-align: center;
    font-size: 20px; font-weight: 400; color: var(--footer-ink);
  }
  .social-title .script { font-family: "Great Vibes", cursive; font-size: 36px; vertical-align: -3px; }
  .social-links { position: absolute; left: 321px; top: 989px; display: flex; gap: 11px; }
  .social-links span { width: 34px; height: 34px; border: 2px solid var(--footer-ink); border-radius: 50%; }
  .footer-rule { position: absolute; left: 235px; top: 1041px; width: 343px; height: 1px; background: #8a7a68; }
  .footer-nav { position: absolute; left: 257px; top: 1062px; width: 300px; display: grid; grid-template-columns: repeat(3, 100px); row-gap: 11px; }
  .footer-nav a { font-size: 8px; font-weight: 500; color: var(--footer-ink); text-align: center; text-decoration: none; }
</style>
</head>
<body>
  <header class="site-header">
    <div class="brand"><span class="brand-dot"></span>LUMERA CAFE</div>
    <nav class="main-nav">
      <span>HOME</span><span class="is-active">ABOUT US</span><span>OUR STORY</span><span>OUR MENU</span><span>EVENTS</span><span>CAREERS</span><span>LOCATION</span><span>CONTACT US</span>
    </nav>
    <div class="book-button">BOOK A TABLE</div>
  </header>

  <div class="hero" role="img" aria-label="Photo of a breakfast plate with salad, smoked salmon, scrambled eggs and flatbread"></div>

  <h1 class="section-title">ABOUT US</h1>
  <p class="about-text">With influences from the Mediterranean, Lumera Café was founded with a great deal of intuition into what makes a dining experience great. Lumera Cafe is a place, where people come to chat, meet up or even work. We set out to offer our guests an experience they wouldn't soon forget and an inventive menu selections all made fresh with quality ingredients and served in a warm and casually comfortable setting.</p>

  <div class="promo-card breakfast" role="img" aria-label="Photo of a breakfast table with eggs, coffee and halloumi">
    <div class="promo-lead">CHECK OUT OUR</div>
    <div class="promo-script">Breakfast</div>
    <div class="cta">FIND OUT MORE <svg viewBox="0 0 7 9"><path d="M1 0.5 L5.5 4.5 L1 8.5" fill="none" stroke="#fff" stroke-width="1.8"/></svg></div>
  </div>
  <div class="promo-card location" role="img" aria-label="Photo of guests inside a busy cafe bar">
    <div class="promo-lead">FIND YOUR NEAREST</div>
    <div class="promo-script">Location</div>
    <div class="cta">FIND OUT MORE <svg viewBox="0 0 7 9"><path d="M1 0.5 L5.5 4.5 L1 8.5" fill="none" stroke="#fff" stroke-width="1.8"/></svg></div>
  </div>

  <div class="menu-banner" role="img" aria-label="Photo of a bowl of hummus with chickpeas and paprika">
    <div class="banner-line1">CUM SOCIIS NATOQUE PENATIBUS ET MAGNIS</div>
    <div class="banner-line2"><span class="script">Spirit</span> <span class="small">OF</span> MEDITERRANEAN</div>
    <div class="banner-line3">DONecpretium LIBERO VELITPRETIUM PORTANULLA CONGUE</div>
    <div class="banner-line4">PRAESENT LAOREET LIBERO PARTURIENT</div>
    <div class="cta">VIEW OUR NEW MENU <svg viewBox="0 0 7 9"><path d="M1 0.5 L5.5 4.5 L1 8.5" fill="none" stroke="#fff" stroke-width="1.8"/></svg></div>
  </div>

  <h2 class="social-title">LIKE US, <span class="script">Love us</span>, SHARE US.</h2>
  <div class="social-links">
    <span aria-label="Social network link"></span><span aria-label="Social network link"></span><span aria-label="Social network link"></span><span aria-label="Video channel link"></span>
  </div>
  <div class="footer-rule"></div>
  <nav class="footer-nav">
    <a>HOME</a><a>OUR MENU</a><a>LOCATION</a>
    <a>ABOUT US</a><a>EVENTS</a><a>CONTACT US</a>
    <a>OUR STORY</a><a>CAREERS</a><a></a>
  </nav>
</body>
</html>
```